Fun, Clean Business Card For Family Focused Travel Agency

I need a business card using specific colors and fonts as in the uploaded files. Ideally, I would like a large image of the logo on the back and all the contact info on the front. Maybe the stars/dots somewhere in a flowy form.

I do want it the contact information to be clear and easy to read. I don't want it to look too busy. Maybe even a bit minimalist.

I plan or ordering the ROUNDED CORNER business cards from Cardwell Press, so please consider that in your design.

Target Market(s)

Families with children, couples, groups of friends

Contact Information for Business Card

Marla Quent, Owner
Marla@TidewayTrips.example
Cell Phone Number 555-218-6034
Office Phone Number 555-647-1295
Specializing in Fablecrest destinations, Goldmere Parkside Resort, Cruises and All-Inclusive Vacations.

Nice but not required:
www.TidewayTrips.example
Facebook, Instagram, Twitter icons with username: TidewayTrips

Font styles to use
Sans Serif

Requirements
Must have
• Please try to use the colors from the logo as much as possible. I understand lighter shades/colors may be needed for some things.
Should not have
• NO SERIF FONTS. That is really the only thing I do not want at all

```html
<!DOCTYPE html>
<html lang="en">
<head>
<meta charset="utf-8">
<title>Tideway Trips – Business Card</title>
<link rel="stylesheet" href="https://fonts.googleapis.com/css2?family=Encode+Sans+Semi+Condensed:wght@700&family=Ubuntu:wght@300;400;500;700&display=swap">
<style>
  :root {
    --navy: #161c28;
    --ink: #0f1626;
    --sea-green: #5a9a7e;
    --white: #ffffff;
    --sun: #e8b23a;
    --coral: #e08a4e;
    --sky: #6aa6d8;
  }
  * { box-sizing: border-box; margin: 0; padding: 0; }
  html, body { width: 1050px; height: 1200px; overflow: hidden; background: var(--white); }
  .sheet { position: relative; width: 1050px; height: 1200px; }

  .card-front {
    position: absolute; left: 0; top: 0; width: 1050px; height: 598px;
    background: var(--navy); color: var(--white); overflow: hidden;
    font-family: "Ubuntu", sans-serif;
  }
  .ribbon { position: absolute; left: 60px; top: 0; width: 97px; height: 130px; }

  .owner-name {
    position: absolute; left: 60px; top: 166px;
    font-family: "Encode Sans Semi Condensed", sans-serif; font-weight: 700;
    font-size: 62px; line-height: 1; color: var(--sea-green);
  }
  .owner-role {
    position: absolute; left: 61px; top: 228px;
    font-family: "Encode Sans Semi Condensed", sans-serif; font-weight: 700;
    font-size: 38px; line-height: 1; color: var(--sea-green);
  }
  .contact-list {
    position: absolute; left: 60px; top: 282px; list-style: none;
    font-size: 28px; font-weight: 300; line-height: 37.5px;
  }
  .specialties {
    position: absolute; left: 58px; top: 428px; width: 560px;
    font-size: 19px; font-weight: 300; line-height: 25px;
  }
  .social-row {
    position: absolute; left: 64px; top: 520px; height: 46px;
    display: flex; align-items: center; font-size: 15.5px; font-weight: 400;
  }
  .social-item { display: flex; align-items: center; }
  .social-item + .social-item { margin-left: 8px; }
  .social-mark {
    width: 43px; height: 43px; border-radius: 5px; background: var(--sea-green);
    margin-right: 14px; flex: none;
  }
  .social-mark.outline { background: none; border: 3px solid var(--sea-green); border-radius: 10px; }
  .globe { width: 46px; height: 46px; margin-right: 8px; flex: none; }

  .travel-illustration {
    position: absolute; left: 740px; top: 24px; width: 310px; height: 554px;
    background:
      radial-gradient(circle at 30% 22%, rgba(232,138,78,0.75), rgba(232,138,78,0) 28%),
      radial-gradient(circle at 82% 30%, rgba(255,255,255,0.35), rgba(255,255,255,0) 30%),
      radial-gradient(circle at 65% 60%, rgba(208,58,58,0.6), rgba(208,58,58,0) 25%),
      radial-gradient(circle at 28% 78%, rgba(90,154,126,0.6), rgba(90,154,126,0) 28%),
      radial-gradient(circle at 78% 85%, rgba(106,166,216,0.55), rgba(106,166,216,0) 28%);
  }

  .card-back {
    position: absolute; left: 0; top: 598px; width: 1050px; height: 602px;
    background: var(--white);
  }
  .brand-symbol {
    position: absolute; left: 40px; top: 140px; width: 300px; height: 300px;
    border-radius: 50%; background: var(--ink);
  }
  .brand-name {
    position: absolute; left: 380px; top: 118px;
    font-family: "Ubuntu", sans-serif; font-weight: 700;
    font-size: 156px; line-height: 170px; color: var(--ink);
  }
</style>
</head>
<body>
<main class="sheet">
  <section class="card-front">
    <svg class="ribbon" viewBox="0 0 97 130" aria-hidden="true">
      <polygon points="0,0 97,0 97,130 48.5,72 0,130" fill="#ffffff"/>
      <polygon points="7,0 90,0 90,112 48.5,62 7,112" fill="#5a9a7e"/>
      <polyline points="12,0 12,100 48.5,56 85,100 85,0" fill="none" stroke="#ffffff" stroke-width="2"/>
    </svg>

    <h1 class="owner-name">MARLA QUENT</h1>
    <p class="owner-role">OWNER</p>

    <ul class="contact-list">
      <li>Marla@TidewayTrips.example</li>
      <li>Cell Phone Number 555-218-6034</li>
      <li>Office Phone Number 555-647-1295</li>
    </ul>

    <p class="specialties">Specializing in Fablecrest destinations, Goldmere Parkside Resort, Cruises and All-Inclusive Vacations</p>

    <div class="social-row">
      <div class="social-item">
        <svg class="globe" viewBox="0 0 46 46" aria-hidden="true">
          <circle cx="23" cy="23" r="20" fill="none" stroke="#5a9a7e" stroke-width="3"/>
          <ellipse cx="23" cy="23" rx="9" ry="20" fill="none" stroke="#5a9a7e" stroke-width="2.5"/>
          <line x1="3" y1="23" x2="43" y2="23" stroke="#5a9a7e" stroke-width="2.5"/>
          <line x1="7" y1="13" x2="39" y2="13" stroke="#5a9a7e" stroke-width="2"/>
          <line x1="7" y1="33" x2="39" y2="33" stroke="#5a9a7e" stroke-width="2"/>
        </svg>
        <span>www.TidewayTrips.example</span>
      </div>
      <div class="social-item"><span class="social-mark"></span><span>TidewayTrips</span></div>
      <div class="social-item"><span class="social-mark outline"></span><span>TidewayTrips</span></div>
      <div class="social-item"><span class="social-mark"></span><span>TidewayTrips</span></div>
    </div>

    <div class="travel-illustration" role="img" aria-label="Travel illustration: flip-flops, airplane, sunset, red suitcase, tickets, life ring, surfboards and sparkles"></div>
  </section>

  <section class="card-back">
    <span class="brand-symbol" aria-hidden="true"></span>
    <p class="brand-name">Tideway<br>Trips</p>
  </section>
</main>
</body>
</html>
```